Hiking Made Simple Outfitter Directory

Hero Section
Image: A serene and picturesque camping landscape with a lake, mountains, and a few trees There is a circle of people sitting around a campfire. The image should be high-quality and visually appealing.
Headline: "Introducing Hikingmadesimple.net's Outfitter Directory"
Subheading: "Join our directory of trusted outfitters and reach a targeted audience of camping enthusiasts."
Call-to-Action (CTA) Button: "Learn More" or "Join Now"
Color scheme: Match hikingmadesimple.net and the logo
Example:
[Image: A serene and picturesque camping landscape with a lake, mountains, and a few trees]
Introducing Hikingmadesimple.net's Outfitter Directory
Join our directory of trusted outfitters and reach a targeted audience of camping enthusiasts.
Learn More
Benefits Section
Image: A group of happy campers sitting around a campfire, roasting marshmallows and telling stories.
Headline: "Benefits of Joining Our Directory"
Bullet points:
"Increase your exposure and visibility to potential customers"
"Book more trips and generate more revenue"
"Access a targeted audience of camping enthusiasts"
Color scheme: match hikingmadesimple.net
Example:
[Image: A group of happy campers sitting around a campfire, roasting marshmallows and telling stories]
Benefits of Joining Our Directory
• Increase your exposure and visibility to potential customers • Book more trips and generate more revenue • Access a targeted audience of camping enthusiasts
Features Section
Image: A screenshot of the directory's search functionality, showing a list of outfitters with their logos, names, and locations.
Headline: "Features of Our Outfitter Directory"
Bullet points:
"Search functionality to find outfitters by location, activity, or type"
"Outfitter profiles with detailed information and reviews"
"Booking system to make it easy for customers to book trips"
Example:
[Image: A screenshot of the directory's search functionality, showing a list of outfitters with their logos, names, and locations]
Features of Our Outfitter Directory
• Search functionality to find outfitters by location, activity, or type • Outfitter profiles with detailed information and reviews • Booking system to make it easy for customers to book trips
CTA Section
Image: A simple and clean design with a prominent call-to-action button.
Headline: "Express Interest in Joining Our Directory"
Call-to-Action (CTA) Button: "Express Interest" or "Join Now"

Example:
[Image: A simple and clean design with a prominent call-to-action button]
Express Interest in Joining Our Directory
Express Interest
Contact Information Section
Image: A simple and clean design with a form to collect contact information.
Headline: "Get in Touch with Us"
Form fields:
Name
Email
Phone
Website

```html
<!DOCTYPE html>
<html lang="en">
<head>
<meta charset="utf-8">
<title>Hiking Made Simple – Outfitter Directory</title>
<link rel="stylesheet" href="https://fonts.googleapis.com/css2?family=Bebas+Neue&family=Poppins:wght@400;500;600&family=Great+Vibes&display=swap">
<style>
:root{
  --orange:#f04b14;
  --orange-band:#ef4a19;
  --teal:#0aa0a3;
  --ink:#1b1b1b;
  --white:#ffffff;
  --field:#ffffff;
  --panel:#f1f1f1;
  --navy:#0f2540;
}
*{box-sizing:border-box;margin:0;padding:0}
html,body{width:1200px;height:3834px;overflow:hidden}
body{position:relative;font-family:"Poppins",sans-serif;color:var(--ink);background:var(--white)}
.abs{position:absolute}
.display{font-family:"Bebas Neue",sans-serif;font-weight:400;letter-spacing:.5px}
.script{font-family:"Great Vibes",cursive;font-size:19px}
.btn{position:absolute;display:flex;align-items:center;justify-content:center;border-radius:30px;color:var(--white);font-weight:500}
.btn--teal{background:var(--teal);font-size:13px}

/* header */
.site-header{left:0;top:0;width:1200px;height:94px;background:var(--white);z-index:3}
.brand{left:137px;top:22px;width:130px;height:130px;border-radius:50%;background:var(--white);box-shadow:0 2px 8px rgba(0,0,0,.15);display:flex;align-items:center;justify-content:center;text-align:center;font-size:15px;font-weight:600;color:var(--navy);line-height:1.2;z-index:4}
.contact-chip{top:25px;display:flex;align-items:center;gap:12px}
.chip-icon{width:46px;height:46px;border-radius:50%;background:var(--orange);display:flex;align-items:center;justify-content:center}
.chip-text{font-size:11px;line-height:1.5}
.chip-text b{font-size:13px;font-weight:600;display:block}
.header-divider{left:827px;top:18px;width:1px;height:56px;background:#d5d5d5}

/* hero */
.hero{left:0;top:94px;width:1200px;height:530px;background:linear-gradient(160deg,#4f5642 0%,#3a3a2a 40%,#5a4e2e 65%,#2d2a22 100%)}
.hero__tent{left:560px;top:300px;width:560px;height:260px;background:radial-gradient(ellipse at center,rgba(206,170,40,.55),rgba(206,170,40,0) 70%)}
.hero__title{left:142px;top:240px;font-size:72px;color:var(--white);line-height:1}
.hero__lead{left:142px;top:324px;width:580px;font-size:20.5px;line-height:31px;color:var(--white)}
.hero__btn{left:142px;top:411px;width:171px;height:54px;background:var(--orange);font-size:17px}

/* photo circles */
.photo-ring{width:453px;height:453px;border-radius:50%;background:var(--white);box-shadow:0 0 14px rgba(0,0,0,.12);display:flex;align-items:center;justify-content:center}
.photo{width:408px;height:408px;border-radius:50%}

.section-label{color:var(--ink)}
.section-title{font-size:35px;color:var(--orange);line-height:1}
.bullets{list-style:none;font-size:13px;line-height:21px}
.bullets li{position:absolute;left:0;display:flex;gap:10px;width:440px}
.bullets svg{flex:none;margin-top:2px}

/* about */
.about{left:0;top:1260px;width:1200px;height:646px;background:linear-gradient(180deg,var(--orange-band) 0%,#ef4c1d 70%,#d9461f 100%);color:var(--white)}
.about h3{font-size:28px;line-height:1;position:absolute;left:143px}
.about p{position:absolute;left:143px;width:418px;font-size:12.5px;line-height:21px}

/* cta band */
.cta-band{left:0;top:2534px;width:1200px;height:317px;background:linear-gradient(180deg,#26303a 0%,#2f3b3a 50%,#243028 100%)}
.cta-band__title{left:0;width:1200px;top:2666px;text-align:center;font-size:37px;color:var(--white)}

/* lower */
.lower{left:0;top:2851px;width:1200px;height:983px;background:linear-gradient(180deg,#eef0f2 0%,#e6e8ea 28%,#b9bfb3 34%,#7b8772 42%,#4a5a45 55%,#2b3e43 70%,var(--navy) 84%,var(--navy) 100%)}
.card{top:2938px;width:220px;height:222px;border-radius:12px;background:var(--white);box-shadow:0 2px 10px rgba(0,0,0,.07);display:flex;flex-direction:column;align-items:center;justify-content:flex-end;padding-bottom:42px;gap:22px;font-size:15.5px;font-weight:500}
.card--active{background:var(--teal);color:var(--white)}
.contact-panel{left:250px;top:3250px;width:705px;height:405px;background:var(--panel);border:5px solid rgba(255,255,255,.85);border-radius:6px}
.contact-title{left:0;width:1200px;top:3290px;text-align:center;font-size:32px}
.title-rule{left:585px;top:3332px;width:30px;height:2px;background:var(--orange)}
.field{background:var(--field);border:1px solid #dedede;font-size:12px;color:#333;padding:8px 14px;height:35px;width:291px}
.field--message{width:584px;height:104px;top:3459px;left:306px}

/* footer */
.footer-item{top:3713px;display:flex;align-items:center;gap:12px;color:var(--white)}
.footer-icon{width:34px;height:34px;border-radius:50%;border:2px solid var(--white);display:flex;align-items:center;justify-content:center;flex:none}
.footer-text{font-size:12px;line-height:16px}
.footer-text b{font-size:14.5px;font-weight:500;display:block}
.footer-sep{top:3710px;width:1px;height:50px;background:rgba(255,255,255,.35)}
.footer-rule{left:141px;top:3792px;width:918px;height:1px;background:rgba(255,255,255,.35)}
.copyright{left:141px;top:3805px;font-size:11px;color:var(--white)}
.social{top:3807px;width:10px;height:10px;border-radius:50%;background:var(--white)}
</style>
</head>
<body>

<header class="abs site-header">
  <div class="abs contact-chip" style="left:649px">
    <div class="chip-icon"><svg width="22" height="22" viewBox="0 0 24 24" fill="none" stroke="#fff" stroke-width="1.8"><path d="M5 3h4l2 5-2.5 1.5a11 11 0 0 0 6 6L16 13l5 2v4a2 2 0 0 1-2 2A17 17 0 0 1 3 5a2 2 0 0 1 2-2z"/></svg></div>
    <div class="chip-text"><b>Call</b>(555) 014-2290</div>
  </div>
  <div class="abs header-divider"></div>
  <div class="abs contact-chip" style="left:861px">
    <div class="chip-icon"><svg width="22" height="22" viewBox="0 0 24 24" fill="none" stroke="#fff" stroke-width="1.8"><rect x="3" y="5" width="18" height="14" rx="2"/><path d="M3 7l9 6 9-6"/></svg></div>
    <div class="chip-text"><b>Email</b>info@hikingmadesimple.net</div>
  </div>
</header>
<div class="abs brand">Hiking<br>Made<br>Simple</div>

<section class="abs hero" role="img" aria-label="Campsite with a yellow tent, backpack and hikers on a forested mountain plateau"></section>
<div class="abs hero__tent"></div>
<h1 class="abs display hero__title">Never Stop Exploring</h1>
<p class="abs hero__lead">Join our directory of trusted outfitters and reach a<br>targeted audience of camping enthusiasts.</p>
<a class="btn hero__btn">Join Now</a>

<!-- benefits -->
<div class="abs photo-ring" style="left:142px;top:712px"><div class="photo" role="img" aria-label="Hiker resting against a white tent on a hillside" style="background:linear-gradient(150deg,#c9c8c0,#8d8a78 50%,#3d4a3a)"></div></div>
<div class="abs script section-label" style="left:683px;top:806px">Our Benefits</div>
<h2 class="abs display section-title" style="left:683px;top:844px">Benefits of Joining Our Directory</h2>
<ul class="abs bullets" style="left:683px;top:892px">
  <li style="top:0"><svg width="19" height="19" viewBox="0 0 20 20" fill="none" stroke="#111" stroke-width="1.6"><path d="M3 2l15 8-15 8 4-8z"/></svg>Increase your exposure and visibility to potential customers</li>
  <li style="top:43px"><svg width="19" height="19" viewBox="0 0 20 20" fill="none" stroke="#111" stroke-width="1.6"><path d="M3 2l15 8-15 8 4-8z"/></svg>Book more trips and generate more revenue</li>
  <li style="top:85px"><svg width="19" height="19" viewBox="0 0 20 20" fill="none" stroke="#111" stroke-width="1.6"><path d="M3 2l15 8-15 8 4-8z"/></svg>Access a targeted audience of camping enthusiasts</li>
</ul>
<a class="btn btn--teal" style="left:685px;top:1024px;width:143px;height:42px">Join Now</a>

<!-- about -->
<section class="abs about" role="img" aria-label="Campsite scene under an orange wash">
  <div class="abs script" style="left:143px;top:138px;color:#fff">About Us</div>
  <h3 class="display" style="top:180px">Who We Are</h3>
  <p style="top:208px">Here at Hiking Made Simple, we love exploring just as much as you do. We have all the best gear to make your adventures possible. Enjoy our site!</p>
  <h3 class="display" style="top:300px">Our Mission</h3>
  <p style="top:328px">We are committed to being there for our customers wherever your adventures should take you.</p>
  <h3 class="display" style="top:398px">Our Vision</h3>
  <p style="top:426px">We carefully select manufacturers that embody our core values of providing the highest quality products with the lowest carbon footprint. We only get one earth to live on, so we must protect it.</p>
</section>
<div class="abs photo-ring" style="left:606px;top:1357px"><div class="photo" role="img" aria-label="Two hikers with backpacks sitting on a rocky summit at sunset" style="background:linear-gradient(180deg,#a9b3bc,#d8cdb8 40%,#4f5a48 65%,#2d2b26)"></div></div>

<!-- features -->
<div class="abs photo-ring" style="left:142px;top:1994px"><div class="photo" role="img" aria-label="Camper sitting in front of a tent on grass with mountains behind" style="background:linear-gradient(180deg,#7f98b8,#6d7c55 40%,#8ba04a 70%,#4d6b2c)"></div></div>
<div class="abs script section-label" style="left:661px;top:2078px">Our Features</div>
<h2 class="abs display section-title" style="left:661px;top:2106px">Features of Our Outfitter Directory</h2>
<ul class="abs bullets" style="left:661px;top:2156px">
  <li style="top:0"><svg width="19" height="19" viewBox="0 0 20 20" fill="none" stroke="#111" stroke-width="1.6"><path d="M3 2l15 8-15 8 4-8z"/></svg>Search functionality to find outfitters by location,<br>activity, or type</li>
  <li style="top:61px"><svg width="19" height="19" viewBox="0 0 20 20" fill="none" stroke="#111" stroke-width="1.6"><path d="M3 2l15 8-15 8 4-8z"/></svg>Outfitter profiles with detailed information and reviews</li>
  <li style="top:104px"><svg width="19" height="19" viewBox="0 0 20 20" fill="none" stroke="#111" stroke-width="1.6"><path d="M3 2l15 8-15 8 4-8z"/></svg>Booking system to make it easy for customers to<br>book trips</li>
</ul>
<a class="btn btn--teal" style="left:661px;top:2323px;width:143px;height:42px">Join Now</a>

<!-- cta band -->
<section class="abs cta-band" role="img" aria-label="Tents in a misty pine forest at dusk"></section>
<div class="abs script" style="left:0;width:1200px;text-align:center;top:2623px;color:#fff">Contact Now</div>
<h2 class="abs display cta-band__title">Express Interest in Joining Our Directory</h2>
<a class="btn btn--teal" style="left:529px;top:2717px;width:142px;height:40px">Join Now</a>

<!-- lower -->
<section class="abs lower" role="img" aria-label="Misty mountain valley landscape"></section>

<div class="abs card" style="left:141px">
  <svg width="58" height="82" viewBox="0 0 58 82" fill="none" stroke="#111" stroke-width="2.4"><rect x="4" y="14" width="50" height="66" rx="8"/><path d="M20 14V6a4 4 0 0 1 4-4h10a4 4 0 0 1 4 4v8"/><rect x="12" y="44" width="34" height="22" rx="3"/><path d="M12 52h34M24 30h10"/></svg>
  Backpacks
</div>
<div class="abs card card--active" style="left:374px">
  <svg width="76" height="92" viewBox="0 0 76 92" fill="none" stroke="#fff" stroke-width="2.4"><path d="M18 6l34 6-4 32-34-6z"/><path d="M8 44h60l-6 8H14z"/><path d="M16 52l40 36M60 52L20 88M14 44l6-38M62 44l-6-32"/></svg>
  Camp Furniture
</div>
<div class="abs card" style="left:604px">
  <svg width="56" height="92" viewBox="0 0 56 92" fill="none" stroke="#111" stroke-width="2.4"><rect x="4" y="4" width="48" height="18" rx="2"/><path d="M18 22v12h20V22M14 34h28"/><path d="M8 50a20 20 0 0 1 40 0v38H8z"/><path d="M28 56c-6 6-6 14 0 16 6-2 6-10 0-16z"/></svg>
  Camp Kitchen
</div>
<div class="abs card" style="left:837px">
  <svg width="84" height="92" viewBox="0 0 84 92" fill="none" stroke="#111" stroke-width="2.4"><path d="M20 60a28 28 0 0 1 10-48M58 14a28 28 0 0 1 8 46M28 82a28 28 0 0 0 30-6"/><rect x="8" y="20" width="18" height="24" rx="4" transform="rotate(-30 17 32)"/><rect x="56" y="20" width="18" height="24" rx="4" transform="rotate(30 65 32)"/><rect x="30" y="62" width="24" height="18" rx="4"/></svg>
  Electronics
</div>

<div class="abs contact-panel"></div>
<h2 class="abs display contact-title">Contact Us</h2>
<div class="abs title-rule"></div>
<div class="abs field" style="left:306px;top:3353px">First Name</div>
<div class="abs field" style="left:603px;top:3353px">Company Email</div>
<div class="abs field" style="left:306px;top:3405px">Phone number</div>
<div class="abs field" style="left:603px;top:3405px">Address</div>
<div class="abs field field--message">Send message</div>
<a class="btn btn--teal" style="left:529px;top:3585px;width:142px;height:42px">Submit</a>

<!-- footer -->
<div class="abs footer-item" style="left:141px">
  <div class="footer-icon"><svg width="16" height="16" viewBox="0 0 24 24" fill="none" stroke="#fff" stroke-width="2"><path d="M5 3h4l2 5-2.5 1.5a11 11 0 0 0 6 6L16 13l5 2v4a2 2 0 0 1-2 2A17 17 0 0 1 3 5a2 2 0 0 1 2-2z"/></svg></div>
  <div class="footer-text">Call us:<b>(555) 014-2290</b></div>
</div>
<div class="abs footer-sep" style="left:352px"></div>
<div class="abs footer-item" style="left:410px">
  <div class="footer-icon"><svg width="16" height="16" viewBox="0 0 24 24" fill="none" stroke="#fff" stroke-width="2"><path d="M12 22s7-7 7-12a7 7 0 0 0-14 0c0 5 7 12 7 12z"/><circle cx="12" cy="10" r="2.5"/></svg></div>
  <div class="footer-text"><b>Lorem Ipsum is simply dummy</b>4180 text of the printing and<br>typesetting industry. CO 80012</div>
</div>
<div class="abs footer-sep" style="left:738px"></div>
<div class="abs footer-item" style="left:805px">
  <div class="footer-icon"><svg width="16" height="16" viewBox="0 0 24 24" fill="none" stroke="#fff" stroke-width="2"><rect x="3" y="5" width="18" height="14" rx="2"/><path d="M3 7l9 6 9-6"/></svg></div>
  <div class="footer-text"><b>info@hikingmadesimple.net</b>Send us your query anytime!</div>
</div>
<div class="abs footer-rule"></div>
<div class="abs copyright">© 2024 HikingMadeSimple LP. All Rights Reserved.</div>
<div class="abs social" style="left:955px"></div>
<div class="abs social" style="left:984px"></div>
<div class="abs social" style="left:1013px"></div>
<div class="abs social" style="left:1047px"></div>

</body>
</html>
```